New Business Card for General Contractor Marketing

Need a business card the is more like a marketing promotion of our services
Must be horizontal orientation, One Sided Only, Max font size, Organize the Services
#1 General Contractor for Realtors
Remodels – Renovations – Repairs
Water & Mold Damage Experts
Painting: Interior/ Exterior
Flooring: Wood / LVT / Carpet
Plumbing: Repairs & Upgrades
Electric: Lights & Energy Efficient Upgrades
Kitchen & Bath Remodels
Fast Inspections Repair Billed Thru Escrow
BrightHarborBuilds.com
555-418-2796

Industry/Entity Type

General Contractor

Contact Information for Business Card

One Sided Only: #1 General Contractor for Realtors Remodels – Renovations – Repairs Water & Mold Damage Experts Painting: Interior/ Exterior Flooring: Wood / LVT / Carpet Plumbing: Repairs & Upgrades Electric: Lights & Energy Efficient Upgrades Kitchen & Bath Remodels Fast Inspections Repair Billed Thru Escrow BrightHarborBuilds.com 555-418-2796

Colors
0054AA
0677BA
7BADD7
CADEEF
E8F1F8

Requirements
Must have
• One Sided Only: #1 General Contractor for Realtors Remodels – Renovations – Repairs Water & Mold Damage Experts Painting: Interior/ Exterior Flooring: Wood / LVT / Carpet Plumbing: Repairs & Upgrades Electric: Lights & Energy Efficient Upgrades Kitchen & Bath Remodels Fast Inspections Repair Billed Thru Escrow BrightHarborBuilds.com 555-418-2796

```html
<!DOCTYPE html>
<html lang="en">
<head>
<meta charset="UTF-8">
<title>BrightHarborBuilds Business Card</title>
<link href="https://fonts.googleapis.com/css2?family=Montserrat:wght@500;600;700;800&display=swap" rel="stylesheet">
<style>
  :root {
    --navy: #1b2a5c;
    --orange: #e8651a;
    --orange-light: #f39a3c;
    --card: #ffffff;
    --page: #ffffff;
    --rule: #c9ccd6;
    --ink-soft: #2a3560;
  }
  * { margin: 0; padding: 0; box-sizing: border-box; }
  html, body {
    width: 1200px; height: 1200px; overflow: hidden;
    background: var(--page);
    font-family: "Montserrat", Arial, sans-serif;
  }
  .card {
    position: absolute; left: 200px; top: 326px;
    width: 798px; height: 460px;
    background: var(--card);
  }
  .headline {
    position: absolute; left: 0; right: 0; top: 28px;
    text-align: center; color: var(--navy);
    font-weight: 800; font-size: 38px; letter-spacing: -0.5px;
  }
  .tagline {
    position: absolute; left: 0; right: 0; top: 78px;
    display: flex; align-items: center; justify-content: center; gap: 12px;
    color: var(--orange); font-weight: 600; font-size: 21px;
  }
  .tagline::before, .tagline::after {
    content: ""; width: 52px; height: 2px; background: var(--orange);
  }
  .hero-art {
    position: absolute; left: 40px; top: 134px;
    width: 306px; height: 136px;
    background: linear-gradient(135deg, #1f3b7a 0%, #274a8e 45%, #f07a22 55%, #e8651a 100%);
    border-radius: 4px;
  }
  .services {
    position: absolute; left: 352px; top: 126px;
    height: 176px; border-left: 2px solid var(--rule);
    padding-left: 10px; list-style: none;
  }
  .service {
    display: flex; align-items: center; gap: 6px;
    height: 31.4px; color: var(--navy);
    font-weight: 700; font-size: 18.5px; white-space: nowrap;
  }
  .service::before {
    content: ""; width: 5px; height: 5px; border-radius: 50%;
    background: var(--orange); margin-right: 3px;
  }
  .service .detail { font-weight: 500; font-size: 17px; }
  .service svg { width: 20px; height: 20px; flex: none; }
  .promo-band {
    position: absolute; left: 40px; top: 328px; width: 714px; height: 30px;
    background: linear-gradient(90deg, rgba(232,101,26,0) 0%, var(--orange) 14%, var(--orange) 86%, rgba(232,101,26,0) 100%);
    display: flex; align-items: center; justify-content: center;
    color: #fff; font-weight: 700; font-size: 19.5px;
  }
  .contact {
    position: absolute; left: 0; right: 0; top: 358px;
    display: flex; align-items: center; justify-content: center; gap: 16px;
  }
  .contact .web { color: var(--orange); font-weight: 700; font-size: 21px; }
  .contact .sep { width: 6px; height: 6px; border-radius: 50%; background: #8a93ad; }
  .contact .phone { color: var(--navy); font-weight: 800; font-size: 28px; letter-spacing: 0.5px; }
</style>
</head>
<body>
  <main class="card">
    <h1 class="headline">#1 General Contractor for Realtors</h1>
    <p class="tagline">Specializing in Remodels, Renovations &amp; Repairs</p>

    <div class="hero-art" role="img" aria-label="Illustration of house rooftops in navy and orange with a worker on the roof, a paint roller and a brush"></div>

    <ul class="services">
      <li class="service">
        <svg viewBox="0 0 20 20"><path d="M10 2 C10 2 4 9 4 13 a6 6 0 0 0 12 0 C16 9 10 2 10 2z" fill="var(--navy)"/><path d="M8 13 a2 2 0 0 0 2 2" stroke="#fff" stroke-width="1.5" fill="none"/></svg>
        Water &amp; Mold Damage Experts
      </li>
      <li class="service">
        <svg viewBox="0 0 20 20"><rect x="3" y="3" width="14" height="14" fill="var(--orange)"/><rect x="5" y="9" width="10" height="1.5" fill="#fff"/><rect x="9" y="5" width="1.5" height="4" fill="#fff"/></svg>
        Kitchen &amp; Bath Remodels
      </li>
      <li class="service">
        <svg viewBox="0 0 20 20"><rect x="3" y="3" width="14" height="6" rx="1" fill="var(--navy)"/><rect x="9" y="9" width="2" height="4" fill="var(--navy)"/><rect x="8" y="13" width="4" height="5" rx="1" fill="var(--orange)"/></svg>
        Interior &amp; Exterior Painting
      </li>
      <li class="service">
        <svg viewBox="0 0 20 20"><circle cx="10" cy="8" r="5" fill="var(--orange-light)"/><rect x="8" y="13" width="4" height="4" rx="1" fill="var(--navy)"/></svg>
        Lights &amp; Energy Efficient Upgrades
      </li>
      <li class="service">
        <svg viewBox="0 0 20 20"><rect x="3" y="3" width="6.5" height="6.5" fill="var(--navy)"/><rect x="10.5" y="3" width="6.5" height="6.5" fill="var(--orange)"/><rect x="3" y="10.5" width="6.5" height="6.5" fill="var(--orange)"/><rect x="10.5" y="10.5" width="6.5" height="6.5" fill="var(--navy)"/></svg>
        Flooring: <span class="detail">Wood / LVT / Carpet</span>
      </li>
      <li class="service">
        <svg viewBox="0 0 20 20"><rect x="4" y="3" width="9" height="5" rx="1" fill="var(--orange)"/><rect x="7" y="8" width="4" height="9" rx="1" fill="var(--orange)"/><rect x="13" y="4" width="3" height="3" fill="var(--navy)"/></svg>
        Plumbing: <span class="detail">Repairs &amp; Upgrades</span>
      </li>
    </ul>

    <div class="promo-band">Fast Inspections • Repairs Billed Through Escrow</div>

    <div class="contact">
      <span class="web">BrightHarborBuilds.com</span>
      <span class="sep"></span>
      <span class="phone">555-418-2796</span>
    </div>
  </main>
</body>
</html>
```